Letterhead & Business Card Design Project

Use existing logo to create a new letterhead and business card design. Looking for something clean modern using color options of black, white and gray. The green from the logo may be used lightly as an accent color.

Target Market(s)

Professional business people

Industry/Entity Type

Business

Requirements
Must have
• Business card with front and back design using existing logo.
Nice to have
• Professional presentation
Clean look
Should not have
• No oil rigs, pumpjacks or clip art.

```html
<!DOCTYPE html>
<html lang="en">
<head>
<meta charset="utf-8">
<title>Meridian Exploration – Business Card</title>
<link rel="stylesheet" href="https://fonts.googleapis.com/css2?family=Marcellus&family=Open+Sans:wght@400&display=swap">
<style>
  :root {
    --stage: #2b2b2b;
    --card-dark: #1c1c1c;
    --card-dark-glow: #3a3a3a;
    --card-light: #f2f2f2;
    --card-light-edge: #d9d9d9;
    --ink-light: #f4f4f4;
    --ink-dark: #222222;
    --ink-muted: #bdbdbd;
    --accent: #35c93a;
    --accent-deep: #13a818;
  }
  * { margin: 0; padding: 0; box-sizing: border-box; }
  html, body { width: 1200px; height: 896px; overflow: hidden; }
  body {
    background: var(--stage);
    display: flex;
    align-items: center;
    justify-content: center;
    gap: 50px;
    font-family: "Open Sans", Arial, sans-serif;
  }
  .card {
    position: relative;
    width: 530px;
    height: 303px;
    border-radius: 3px;
    overflow: hidden;
    box-shadow: 0 12px 30px rgba(0,0,0,.55);
  }

  /* Company name placeholder + accent rule */
  .company-name {
    font-family: "Marcellus", serif;
    font-weight: 400;
    line-height: 1;
    white-space: nowrap;
  }
  .accent-rule {
    height: 1px;
    background: var(--accent);
  }

  /* Back card */
  .card-back { background: radial-gradient(ellipse at 55% 55%, var(--card-dark-glow), var(--card-dark) 75%); }
  .card-back .header {
    position: absolute; inset: 0 0 auto 0; height: 118px;
    background: linear-gradient(180deg, var(--card-light), var(--card-light-edge));
  }
  .card-back .brand {
    position: absolute; left: 34px; top: 44px; width: 220px;
  }
  .card-back .company-name { font-size: 17px; color: var(--ink-dark); letter-spacing: 1px; }
  .card-back .accent-rule { margin-top: 10px; width: 200px; }
  .card-back .holder {
    position: absolute; right: 30px; top: 84px; text-align: right;
    font-family: "Marcellus", serif;
  }
  .holder .holder-name { font-size: 21px; color: var(--ink-dark); font-variant: small-caps; letter-spacing: 1px; line-height: 1.2; }
  .holder .holder-role { font-size: 12px; color: var(--ink-muted); letter-spacing: 3px; margin-top: 10px; }
  .contact-list {
    position: absolute; left: 34px; bottom: 30px; list-style: none;
    color: var(--ink-light); font-size: 12.5px;
  }
  .contact-list li { display: flex; align-items: flex-start; gap: 12px; margin-top: 7px; line-height: 1.35; }
  .contact-list svg { width: 13px; height: 13px; flex: none; margin-top: 2px; fill: var(--ink-light); }

  /* Front card */
  .card-front { background: radial-gradient(ellipse at 55% 40%, var(--card-dark-glow), var(--card-dark) 75%); }
  .card-front .brand {
    position: absolute; left: 0; right: 0; top: 112px;
    display: flex; flex-direction: column; align-items: center;
  }
  .card-front .company-name { font-size: 32px; color: var(--ink-light); letter-spacing: 2px; }
  .card-front .accent-rule { margin-top: 16px; width: 380px; }
  .card-front .accent-band {
    position: absolute; left: 0; right: 0; bottom: 0; height: 20px;
    background: linear-gradient(180deg, var(--accent), var(--accent-deep));
  }
</style>
</head>
<body>

  <article class="card card-back">
    <div class="header"></div>
    <div class="brand">
      <div class="company-name">Meridian Exploration</div>
      <div class="accent-rule"></div>
    </div>
    <div class="holder">
      <div class="holder-name">Grant Ellison</div>
      <div class="holder-role">manager</div>
    </div>
    <ul class="contact-list">
      <li>
        <svg viewBox="0 0 16 16" aria-hidden="true"><path d="M3.5 1l2.5 3-1.6 1.6c.9 2 2.5 3.6 4.5 4.5L10.5 8.5l3 2.5-1.5 3C6.5 14 2 9.5 2 3z"/></svg>
        <span>555.014.2270</span>
      </li>
      <li>
        <svg viewBox="0 0 16 16" aria-hidden="true"><rect x="2" y="6" width="12" height="8" rx="1"/><rect x="4" y="2" width="8" height="3"/></svg>
        <span>555.014.2271</span>
      </li>
      <li>
        <svg viewBox="0 0 16 16" aria-hidden="true"><path d="M8 1a7 7 0 100 14A7 7 0 008 1zm0 1.5c.8 0 1.8 1.7 2 4.5H6c.2-2.8 1.2-4.5 2-4.5zM2.6 7h2c.1-1.8.5-3.3 1.1-4.2A5.5 5.5 0 002.6 7zm7.7-4.2c.6.9 1 2.4 1.1 4.2h2a5.5 5.5 0 00-3.1-4.2zM2.6 9a5.5 5.5 0 003.1 4.2c-.6-.9-1-2.4-1.1-4.2zm3.4 0c.2 2.8 1.2 4.5 2 4.5s1.8-1.7 2-4.5zm5.4 0c-.1 1.8-.5 3.300-1.1 4.2A5.5 5.5 0 0013.4 9z"/></svg>
        <span>meridianexploration.com</span>
      </li>
      <li>
        <svg viewBox="0 0 16 16" aria-hidden="true"><path d="M8 1a5 5 0 00-5 5c0 3.8 5 9 5 9s5-5.2 5-9a5 5 0 00-5-5zm0 7a2 2 0 110-4 2 2 0 010 4z"/></svg>
        <span>4410 North Park Ave Suite 210 Fairview,<br>Oklahoma 74000</span>
      </li>
    </ul>
  </article>

  <article class="card card-front">
    <div class="brand">
      <div class="company-name">Meridian Exploration</div>
      <div class="accent-rule"></div>
    </div>
    <div class="accent-band"></div>
  </article>

</body>
</html>
```